Redesign Business Cards, Attached

Please read instructions carefully. If you have any questions send a message before submitting your ONE design. Please redesign attached business cards. Double sided. Use same content and descriptions. Use black, silver, crimson red and gold colors. My only issue with the attached design is the background colors. I like the layout as-is. I can provide the individual pictures on the back side later. Do not submit more than one design. One submission shall include both front and back. Do not submit front and back separately. A second project will be launched to create a matching post card after completion of this.
Industry/Entity Type
see description and attachments.
Contact Information for Business Card
Requirements
Must have
- see description and attachments.
Nice to have
Should not have

```html
<!DOCTYPE html>
<html lang="en">
<head>
<meta charset="utf-8">
<title>Bluewater Helm – Business Card</title>
<link href="https://fonts.googleapis.com/css2?family=Arimo:wght@400;700&display=swap" rel="stylesheet">
<style>
  :root{
    --stage:#1a1a1a;
    --card-white:#ffffff;
    --card-black:#050505;
    --gold:#d4a215;
    --crimson:#a3132b;
    --silver:#c3c7cc;
    --silver-light:#e9ebee;
    --ink:#111111;
  }
  *{margin:0;padding:0;box-sizing:border-box}
  html,body{width:1200px;height:963px;overflow:hidden}
  body{
    background:var(--stage);
    font-family:"Arimo",Arial,sans-serif;
    display:flex;flex-direction:column;align-items:center;justify-content:center;gap:56px;
  }
  .card{
    position:relative;width:700px;height:400px;border-radius:22px;overflow:hidden;
    box-shadow:0 18px 40px rgba(0,0,0,.55);
  }
  .card--front{background:var(--card-white);color:var(--ink);border-top:6px solid var(--crimson)}
  .card--back{
    background:var(--card-black);display:flex;align-items:center;justify-content:center;
    border:2px solid var(--silver);
  }

  .brand{display:flex;align-items:center;gap:14px}
  .brand__dot{width:42px;height:42px;border-radius:50%;background:var(--crimson);flex:none}
  .brand__name{font-weight:700;font-size:21px;line-height:1.2;text-transform:uppercase;letter-spacing:.06em}
  .card--front .brand{position:absolute;left:120px;top:52px}
  .card--front .brand__name{color:var(--ink)}
  .card--back .brand{flex-direction:column;gap:18px;text-align:center}
  .card--back .brand__dot{width:60px;height:60px}
  .card--back .brand__name{color:var(--silver);font-size:26px}

  .holder{position:absolute;right:62px;top:140px;text-align:right}
  .holder__name{color:var(--gold);font-weight:700;font-size:30px;letter-spacing:.04em;text-transform:uppercase}
  .holder__role{font-size:21px;line-height:1.3;margin-top:4px}
  .accent-bar{position:absolute;right:0;top:180px;width:22px;height:66px;background:var(--crimson)}

  .contact{position:absolute;left:46px;bottom:52px;list-style:none}
  .contact__item{display:flex;align-items:center;gap:12px;font-size:21px;line-height:1.5}
  .contact__icon{width:22px;height:22px;flex:none}

  .faint-mark{
    position:absolute;right:90px;bottom:-120px;width:240px;height:240px;border-radius:50%;
    background:linear-gradient(160deg,var(--silver-light),#f6f7f8);
  }
</style>
</head>
<body>
  <section class="card card--front" aria-label="Business card front">
    <div class="faint-mark" aria-hidden="true"></div>
    <div class="brand">
      <span class="brand__dot" aria-hidden="true"></span>
      <span class="brand__name">Bluewater Helm<br>Boat Training &amp; Charters</span>
    </div>
    <div class="holder">
      <p class="holder__name">Dana R. Whitlow</p>
      <p class="holder__role">USCG Licensed Captain<br>Certified Instructor</p>
    </div>
    <div class="accent-bar" aria-hidden="true"></div>
    <ul class="contact">
      <li class="contact__item">
        <svg class="contact__icon" viewBox="0 0 22 22" aria-hidden="true"><circle cx="11" cy="11" r="11" fill="var(--gold)"/><path d="M7.5 6.5l2 0 1 2.6-1.3 1c.6 1.3 1.5 2.2 2.8 2.8l1-1.3 2.6 1v2c0 .6-.5 1-1 1-4.6-.3-7.8-3.5-8.1-8.1 0-.5.4-1 1-1z" fill="#fff"/></svg>
        (555) 014-2288
      </li>
      <li class="contact__item">
        <svg class="contact__icon" viewBox="0 0 22 22" aria-hidden="true"><circle cx="11" cy="11" r="11" fill="var(--gold)"/><rect x="5.5" y="7" width="11" height="8" fill="none" stroke="#fff" stroke-width="1.4"/><path d="M5.5 7l5.5 4.5L16.5 7" fill="none" stroke="#fff" stroke-width="1.4"/></svg>
        hello@bluewaterhelm.com
      </li>
      <li class="contact__item">
        <svg class="contact__icon" viewBox="0 0 22 22" aria-hidden="true"><circle cx="11" cy="11" r="11" fill="var(--gold)"/><circle cx="11" cy="11" r="5.5" fill="none" stroke="#fff" stroke-width="1.3"/><ellipse cx="11" cy="11" rx="2.4" ry="5.5" fill="none" stroke="#fff" stroke-width="1.2"/><path d="M5.5 11h11" stroke="#fff" stroke-width="1.2"/></svg>
        www.bluewaterhelm.com
      </li>
    </ul>
  </section>

  <section class="card card--back" aria-label="Business card back">
    <div class="brand">
      <span class="brand__dot" aria-hidden="true"></span>
      <span class="brand__name">Bluewater Helm<br>Boat Training &amp; Charters</span>
    </div>
  </section>
</body>
</html>
```